Brightmere email header for parts

We sell parts to the construction equipment industry. We want a header for our emails that reflect what we do. I will include what we have now but want something for parts only. Added a lot of pictures just so you can look through what we do.

```html
<!DOCTYPE html>
<html lang="en">
<head>
<meta charset="utf-8">
<title>Brightmere Parts Email Header</title>
<link rel="stylesheet" href="https://fonts.googleapis.com/css2?family=Anton&family=League+Spartan:wght@600;700&family=Montserrat:wght@800&display=swap">
<style>
  :root {
    --page-bg: #e0e0e0;
    --white: #ffffff;
    --ink: #111111;
    --brand-red: #ff0000;
    --charcoal: #1b1b1d;
    --charcoal-light: #2a2a2d;
  }
  * { margin: 0; padding: 0; box-sizing: border-box; }
  html, body {
    width: 1200px;
    height: 1200px;
    overflow: hidden;
    background: var(--page-bg);
  }
  .email-header {
    position: absolute;
    left: 58px;
    top: 371px;
    width: 1084px;
    height: 411px;
    display: block;
  }
  .headline-top { font-family: "Anton", "Impact", sans-serif; fill: var(--ink); }
  .headline-mid { font-family: "League Spartan", "Futura", sans-serif; font-weight: 600; fill: var(--brand-red); }
  .headline-main { font-family: "League Spartan", "Futura", sans-serif; font-weight: 700; fill: var(--white); }
  .phone-number { font-family: "Anton", "Impact", sans-serif; fill: var(--white); }
  .web-address { font-family: "Montserrat", "Arial", sans-serif; font-weight: 800; fill: var(--white); }
  .brand-name { font-family: "League Spartan", "Futura", sans-serif; font-weight: 700; fill: var(--white); }
  .band-red { fill: var(--brand-red); }
  .panel-dark { fill: url(#darkPanel); }
  .diamond-frame { fill: var(--white); stroke: var(--brand-red); stroke-width: 12; }
  .diamond-grid { fill: var(--charcoal); }
</style>
</head>
<body>
<svg class="email-header" viewBox="0 0 1745 661" xmlns="http://www.w3.org/2000/svg" aria-label="Brightmere replacement parts email header">
  <defs>
    <linearGradient id="darkPanel" x1="0" y1="0" x2="1" y2="1">
      <stop offset="0" stop-color="#2a2a2d"/>
      <stop offset="1" stop-color="#1b1b1d"/>
    </linearGradient>
    <linearGradient id="yellowPart" x1="0" y1="0" x2="1" y2="1">
      <stop offset="0" stop-color="#f0c93a"/>
      <stop offset="1" stop-color="#c99a17"/>
    </linearGradient>
    <linearGradient id="blackPart" x1="0" y1="0" x2="1" y2="1">
      <stop offset="0" stop-color="#4a4a4e"/>
      <stop offset="1" stop-color="#1a1a1c"/>
    </linearGradient>
    <clipPath id="bannerClip"><rect width="1745" height="661"/></clipPath>
    <clipPath id="tileTop"><polygon points="1429,-47 1604,128 1429,303 1254,128"/></clipPath>
    <clipPath id="tileLeft"><polygon points="1217,164 1386,333 1217,502 1048,333"/></clipPath>
    <clipPath id="tileRight"><polygon points="1637,166 1809,338 1637,510 1465,338"/></clipPath>
    <clipPath id="tileBottom"><polygon points="1432,368 1602,538 1432,708 1262,538"/></clipPath>
  </defs>

  <g clip-path="url(#bannerClip)">
    <rect class="base" width="1745" height="661" fill="var(--white)"/>

    <!-- lower dark panel -->
    <rect class="panel-dark" x="0" y="416" width="1300" height="245"/>

    <!-- red headline band -->
    <rect class="band-red" x="0" y="271" width="1110" height="145"/>

    <!-- red contact strip -->
    <polygon class="band-red" points="448,563 1420,563 1420,661 352,661"/>

    <!-- diamond grid backdrop -->
    <polygon class="diamond-grid" points="1427,-89 1847,333 1427,755 1007,333"/>

    <!-- product tiles -->
    <g class="product-tile">
      <polygon class="diamond-frame" points="1429,-55 1612,128 1429,311 1246,128"/>
      <rect clip-path="url(#tileTop)" x="1334" y="70" width="190" height="100" rx="10" fill="url(#yellowPart)" role="img" aria-label="Yellow excavator side cover panel"/>
    </g>
    <g class="product-tile">
      <polygon class="diamond-frame" points="1217,156 1394,333 1217,510 1040,333"/>
      <rect clip-path="url(#tileLeft)" x="1142" y="258" width="140" height="150" rx="30" fill="url(#blackPart)" role="img" aria-label="Black track drive motor with sprocket"/>
    </g>
    <g class="product-tile">
      <polygon class="diamond-frame" points="1637,158 1817,338 1637,518 1457,338"/>
      <rect clip-path="url(#tileRight)" x="1567" y="263" width="140" height="150" rx="20" fill="url(#yellowPart)" role="img" aria-label="Yellow final drive assembly"/>
    </g>
    <g class="product-tile">
      <polygon class="diamond-frame" points="1432,360 1610,538 1432,716 1254,538"/>
      <rect clip-path="url(#tileBottom)" x="1332" y="488" width="200" height="95" rx="24" fill="url(#blackPart)" role="img" aria-label="Undercarriage parts: rollers, idler and sprocket"/>
    </g>

    <!-- headline -->
    <text class="headline-top" x="45" y="153" font-size="114" textLength="1020" lengthAdjust="spacingAndGlyphs">REPLACEMENT PARTS</text>
    <text class="headline-mid" x="50" y="251" font-size="112" textLength="1008" lengthAdjust="spacingAndGlyphs">FOR CUSTOM BUILT</text>
    <text class="headline-main" x="60" y="398" font-size="146" textLength="930" lengthAdjust="spacingAndGlyphs">WATER TANKS</text>

    <!-- phone -->
    <g class="phone-icon">
      <circle cx="464" cy="500" r="37" fill="var(--brand-red)"/>
      <path d="M450 478 l9 -3 l7 15 l-7 5 q4 10 13 15 l6 -7 l14 8 l-3 9 q-3 6 -11 5 q-22 -5 -32 -30 q-2 -11 4 -17 z" fill="var(--white)"/>
    </g>
    <text class="phone-number" x="525" y="543" font-size="94" textLength="575" lengthAdjust="spacingAndGlyphs">555-014-2290</text>

    <!-- web -->
    <text class="web-address" x="445" y="610" font-size="44" textLength="730" lengthAdjust="spacingAndGlyphs">www.brightmereparts.com</text>

    <!-- brand -->
    <text class="brand-name" x="48" y="613" font-size="42" textLength="257" lengthAdjust="spacingAndGlyphs">BRIGHTMERE</text>
  </g>
</svg>
</body>
</html>
```